Linen Sparrow- Hand made fashion accessories

Linen sparrow is a new business that will be selling hand made fashion accessories for women such as bags, baskets, knecklaces etc. The items are all hand made from Africa. I would like natural colors leaning more to the cardboard rustic look. I would like the card to look simple but elegant at the same time.

Industry/Entity Type

Business

Contact Information for Business Card

www.linensparrow-example.com.au
sales@linensparrow-example.com.au
Tel: 0427586302

Font styles to use
Decorative
Script

Requirements
Must have
• Earthy and rustic colours. Straw, cardboard etc. Fine black cursive print. One side of card only name
• second side website, email and tel.
Should not have
• No need to have any description of what business sells or does. No pictures of anything.

```html
<!DOCTYPE html>
<html lang="en">
<head>
<meta charset="utf-8">
<title>Linen Sparrow – Business Card</title>
<link rel="stylesheet" href="https://fonts.googleapis.com/css2?family=Arimo:wght@400;700&display=swap">
<style>
  :root {
    --page: #f1ece3;
    --kraft: #d8c09a;
    --kraft-light: #e3cfad;
    --kraft-deep: #c9ad82;
    --bark: #3a2a1c;
    --bark-deep: #2c1f14;
    --straw: #efe3c8;
    --seal-edge: #b89a6e;
    --ink: #2a1d12;
    --ink-soft: #4a3726;
    --rule: 2px;
  }
  * { box-sizing: border-box; margin: 0; padding: 0; }
  html, body {
    width: 1200px; height: 780px; overflow: hidden;
    background: var(--page);
    font-family: "Arimo", Arial, sans-serif;
  }
  .stage {
    position: relative; width: 1200px; height: 780px;
    display: flex; align-items: center; justify-content: center; gap: 60px;
  }
  .card {
    position: relative; width: 500px; height: 290px; overflow: hidden;
    box-shadow: 0 6px 18px rgba(58, 42, 28, .22);
  }
  .card--front {
    background: linear-gradient(135deg, var(--kraft-light) 0%, var(--kraft) 55%, var(--kraft-deep) 100%);
  }
  .card--back {
    background: linear-gradient(135deg, var(--bark) 0%, var(--bark-deep) 100%);
  }

  /* vertical band flanked by fine parallel rules */
  .band { position: absolute; top: 0; bottom: 0; }
  .band::before, .band::after {
    content: ""; position: absolute; top: 0; bottom: 0; width: var(--rule);
  }
  .band::before { left: -8px; }
  .band::after { right: -8px; }

  .card--front .band { left: 92px; width: 116px; background: var(--bark); }
  .card--front .band::before, .card--front .band::after { background: var(--bark); }

  .card--back .band {
    left: 192px; width: 116px;
    background: linear-gradient(135deg, var(--kraft-light), var(--kraft));
  }
  .card--back .band::before, .card--back .band::after { background: var(--kraft-light); }

  .seal {
    position: absolute; top: 50%; width: 156px; height: 156px; border-radius: 50%;
    background: var(--straw);
    border: 1px solid var(--seal-edge);
    transform: translate(-50%, -50%);
    display: flex; align-items: center; justify-content: center; text-align: center;
  }
  .card--front .seal { left: 150px; }
  .card--back .seal { left: 250px; }
  .seal__name {
    font-size: 22px; font-weight: 400; color: var(--ink); line-height: 1.15;
  }

  .contact {
    position: absolute; left: 244px; top: 92px; color: var(--ink);
  }
  .contact__name { font-size: 20px; font-weight: 700; letter-spacing: -.2px; line-height: 1.1; }
  .contact__role { font-size: 14px; color: var(--ink-soft); margin-top: 2px; }
  .contact__list {
    list-style: none; margin-top: 20px;
    font-size: 13px; line-height: 1.5; color: var(--ink-soft);
  }
</style>
</head>
<body>
<main class="stage">
  <section class="card card--front" aria-label="Card front">
    <div class="band"></div>
    <div class="seal"><span class="seal__name">Linen<br>Sparrow</span></div>
    <div class="contact">
      <p class="contact__name">EMPLOYEE NAME</p>
      <p class="contact__role">Development Manager</p>
      <ul class="contact__list">
        <li>0427586302</li>
        <li>sales@linensparrow-example.com.au</li>
        <li>www.linensparrow-example.com.au</li>
      </ul>
    </div>
  </section>

  <section class="card card--back" aria-label="Card back">
    <div class="band"></div>
    <div class="seal"><span class="seal__name">Linen<br>Sparrow</span></div>
  </section>
</main>
</body>
</html>
```